High end cable company busines card and letterhead

Dear designers,
We assemble high end audio cables that cost a couple of hundred dollars per piece and we are improving the looks of the product.
When people buy a cable they get a leather pouch with the invoice (letterhead) , a business card of the maker and also a quality control card  / warranty card.
The quality control card  is the same size as a business card and the back of the quality control card is the same back as the business card. So we need 4 things:
-1 back of a business card
-1 front of a business card (a file where we can change the name and details of the worker)
-1 quality control front (I will add a photo of an example)
-1 letterhead
We want to make letterpress business cards and use shiny foil for the logo’s. We like the colors black and copper or black and gold for the back. The front of the business card can also be black, copper and white but it does not have to be those colors. We want people to have the feeling that they bought something expensive and high quality.
The front of the quality control card has to be white so we can check things off with a sharpie / pen.
What has to be on the cards:
Business card:
- Our Logo
-Text: Meet the maker (people get the business card of the one who made the cable)
-Name
-Address
-Website (www.tarvelinkaudio.com)
-Email address
-Text: For any advise or questions about your cable feel free to contact me.
What has to be on the quality control card:
-Our logo
-Text: quality controll and warranty card (small at the bottom)
-text:
Assembled by:________________
Date: ______-______-____________
QC by:_________________________

Assembly QC [   ]
Measurement QC [   ]
Aesthetics [   ]
(The box [    ] is for the initials of the person that does the QC, it can also be a line or something else)
The letterhead can be your own idea as long as it looks luxurious.
You can download our logo. We have a black one and gold / black but you can change the Color to Match your design. (For instance copper or something) There is also a white one that can be used with the icon on the left.
Some links of stuff we like:
-https://vidlumo.example/k3RzQ81wXyT (The looks of this card maybe a bit less busy looking)
-https://b.shopvarna.com/_qTrwBxe
-https://b.shopvarna.com/_qHp4Lud
-https://b.shopvarna.com/_qZeyi71

```html
<!DOCTYPE html>
<html lang="en">
<head>
<meta charset="utf-8">
<title>Tarvelink — Business Card</title>
<link href="https://fonts.googleapis.com/css2?family=Montserrat:wght@400;500;600&family=Lora:ital@1&display=swap" rel="stylesheet">
<style>
  :root {
    --stage: #d9d9db;
    --card: #1a1818;
    --card-deep: #121111;
    --gold: #d9a91c;
    --gold-soft: #c99a22;
    --white: #f2f2f2;
    --muted: #d8d8d8;
  }
  * { box-sizing: border-box; margin: 0; padding: 0; }
  html, body {
    width: 1200px; height: 800px; overflow: hidden;
    background: radial-gradient(ellipse at 45% 35%, #ececee 0%, var(--stage) 60%, #c4c4c6 100%);
    font-family: "Montserrat", sans-serif;
  }
  .canvas {
    width: 1200px; height: 800px;
    display: flex; align-items: center; justify-content: center; gap: 48px;
  }
  .card {
    width: 530px; height: 303px;
    background: var(--card);
    border-bottom: 3px solid var(--gold);
    border-right: 2px solid var(--gold);
    box-shadow: 0 18px 30px rgba(0,0,0,0.28);
    position: relative;
    overflow: hidden;
  }

  /* Front */
  .front .brand {
    position: absolute; left: 40px; top: 0; bottom: 60px; width: 230px;
    display: flex; align-items: center; gap: 10px;
    white-space: nowrap;
  }
  .brand-square { width: 12px; height: 12px; background: var(--gold); flex: none; }
  .front .brand-name {
    font-weight: 500; font-size: 20px; letter-spacing: 5px; color: var(--white);
  }
  .contact {
    position: absolute; left: 300px; top: 40px; right: 20px;
  }
  .contact-name {
    font-weight: 600; font-size: 20px; letter-spacing: 1px; color: var(--white);
    white-space: nowrap;
  }
  .contact-role {
    font-weight: 500; font-size: 13px; color: var(--gold); margin: 2px 0 14px;
  }
  .contact-list { list-style: none; }
  .contact-list li {
    display: flex; align-items: flex-start; gap: 10px;
    font-size: 11.5px; line-height: 15px; color: var(--muted); margin-bottom: 5px;
    white-space: nowrap;
  }
  .contact-list svg { width: 12px; height: 12px; flex: none; margin-top: 2px; }
  .tagline {
    position: absolute; left: 0; right: 0; bottom: 26px; text-align: center;
    font-family: "Lora", serif; font-style: italic; font-size: 12.5px; color: var(--gold-soft);
  }

  /* Back */
  .back { background: linear-gradient(135deg, var(--card) 0%, var(--card-deep) 100%); }
  .back .brand {
    position: absolute; inset: 0;
    display: flex; align-items: center; justify-content: center; gap: 16px;
    white-space: nowrap;
  }
  .back .brand-square { width: 20px; height: 20px; }
  .back .brand-name {
    font-weight: 500; font-size: 36px; letter-spacing: 12px; color: var(--gold);
  }
</style>
</head>
<body>
<main class="canvas">
  <section class="card front" aria-label="Business card front">
    <div class="brand">
      <span class="brand-square"></span>
      <span class="brand-name">TARVELINK</span>
    </div>
    <div class="contact">
      <p class="contact-name">DANIEL ROERIG</p>
      <p class="contact-role">President</p>
      <ul class="contact-list">
        <li>
          <svg viewBox="0 0 12 12" fill="none" stroke="#d9a91c" stroke-width="1.2"><path d="M6 11s4-4 4-6.5A4 4 0 0 0 2 4.5C2 7 6 11 6 11z"/><circle cx="6" cy="4.5" r="1.3"/></svg>
          <span>1420 Alder Court<br>Juneau, Alaska 34610</span>
        </li>
        <li>
          <svg viewBox="0 0 12 12" fill="none" stroke="#d9a91c" stroke-width="1.2"><path d="M2.5 1.5l2 .3.8 2.3-1.2 1a6 6 0 0 0 2.8 2.8l1-1.2 2.3.8.3 2c-4.5.5-8.5-3.5-8-8z"/></svg>
          <span>369-555-0148</span>
        </li>
        <li>
          <svg viewBox="0 0 12 12" fill="none" stroke="#d9a91c" stroke-width="1.2"><rect x="1" y="2.5" width="10" height="7"/><path d="M1 2.5l5 4 5-4"/></svg>
          <span>info@tarvelinkaudio.com</span>
        </li>
        <li>
          <svg viewBox="0 0 12 12" fill="none" stroke="#d9a91c" stroke-width="1.2"><circle cx="6" cy="6" r="5"/><path d="M1 6h10M6 1c-2.5 3-2.5 7 0 10M6 1c2.5 3 2.5 7 0 10"/></svg>
          <span>tarvelinkaudio.com</span>
        </li>
      </ul>
    </div>
    <p class="tagline">For any advise or questions about your cable feel free to contact me.</p>
  </section>

  <section class="card back" aria-label="Business card back">
    <div class="brand">
      <span class="brand-square"></span>
      <span class="brand-name">TARVELINK</span>
    </div>
  </section>
</main>
</body>
</html>
```